New cool to-go cup for KELMO Coffee

UPDATE MARCH 18: Please read the attached document "Design ideas - Front" with a mock-up of the design we are looking for. And please don't change the logo.

We are looking for a new cool design for our to-go cups in kraft paper (same style as the attached photo).

The idea:

We have three different cups sizes: 6oz, 8oz and 12oz. We call them “Tiny-Lark” (6oz), “Mid-Wren” (8oz) and “Tall-heron” (12oz) (refers to the size in milliliters). We would like to include this in the cup design. Please see the attached sketch of the idea ("Design ideas - Front").

The backside of the cup should have the attached text and logo ("Design ideas - Back").

But other ideas are also very welcome too! Maybe just a simple cup with the logo.

Please keep the design very minimalistic. The more simple the better.

Target Market(s)

Young urban people

Industry/Entity Type

Coffee shop

Font styles to use
Sans Serif

Requirements
Must have
• Kraft paper cups

```html
<!DOCTYPE html>
<html lang="en">
<head>
<meta charset="utf-8">
<title>KELMO Coffee – To-go Cup Sleeve</title>
<link rel="stylesheet" href="https://fonts.googleapis.com/css2?family=Poppins:wght@400;500;600&display=swap">
<style>
  :root {
    --brown: #3c2418;
    --kraft: #a87b52;
    --paper: #ffffff;
    --lettering-tint: #e8ddd4;
    --guide: #a0764a;
    --bleed: #e0442c;
    --margin: #1f7a3a;
  }
  * { margin: 0; padding: 0; box-sizing: border-box; }
  html, body { width: 1200px; height: 857px; overflow: hidden; background: var(--paper); }
  body { font-family: "Poppins", sans-serif; color: var(--brown); position: relative; }

  .guide-v { position: absolute; left: 858px; top: 0; height: 857px; border-left: 1.5px dashed var(--guide); }
  .guide-h { position: absolute; left: 0; top: 467px; width: 858px; border-top: 1.5px dashed var(--guide); }

  .side-label {
    position: absolute; left: 27px; width: 50px; height: 209px;
    background: var(--brown); color: var(--paper);
    display: flex; align-items: center; justify-content: center;
  }
  .side-label span {
    transform: rotate(-90deg); white-space: nowrap;
    font-size: 25px; font-weight: 400; letter-spacing: 1px;
  }
  .side-label.front { top: 153px; }
  .side-label.back { top: 546px; }

  .size-card {
    position: absolute; top: 80px; width: 196px; height: 354px;
    border: 1.5px solid var(--brown); border-radius: 98px 98px 0 0;
  }
  .size-card .brand-ring {
    position: absolute; left: 6px; top: 8px; width: 182px; height: 182px;
    border: 3.5px solid var(--brown); border-radius: 50%;
    display: flex; align-items: center; justify-content: center;
  }
  .brand-name { font-weight: 600; color: var(--brown); text-align: center; line-height: 1.1; }
  .size-card .brand-name { font-size: 26px; }
  .size-card .size-lettering {
    position: absolute; left: 20px; top: 203px; width: 154px; height: 87px;
    background: var(--lettering-tint);
  }
  .size-card .size-band {
    position: absolute; left: 0; right: 0; top: 295px; height: 39px;
    background: var(--brown); color: var(--paper);
    display: flex; justify-content: space-between; align-items: center;
    padding: 0 20px; font-size: 21px; font-weight: 400;
  }
  .card-1 { left: 108px; }
  .card-2 { left: 369px; }
  .card-3 { left: 630px; }

  .back-panel { position: absolute; top: 510px; width: 196px; text-align: center; }
  .back-panel .brand-ring {
    width: 90px; height: 90px; margin: 0 auto;
    border: 2.5px solid var(--brown); border-radius: 50%;
    display: flex; align-items: center; justify-content: center;
  }
  .back-panel .brand-name { font-size: 14px; }
  .back-panel .story { margin-top: 24px; font-size: 17px; line-height: 20px; font-weight: 400; }
  .back-panel .web { margin-top: 4px; font-size: 17px; font-weight: 600; }
  .back-panel .social { margin-top: 6px; font-size: 17px; font-weight: 600; }
  .back-1 { left: 108px; }
  .back-2 { left: 369px; }
  .back-3 { left: 630px; }

  .die-cut-title {
    position: absolute; left: 902px; top: 104px; width: 208px; height: 49px;
    background: var(--brown); color: var(--paper);
    display: flex; align-items: center; justify-content: center;
    font-size: 28px; font-weight: 500; letter-spacing: 1px;
  }
  .die-cut-art { position: absolute; left: 0; top: 0; }
  .die-cut-art text { font-family: "Poppins", sans-serif; }
</style>
</head>
<body>
  <div class="guide-v"></div>
  <div class="guide-h"></div>

  <div class="side-label front"><span>FRONT SIDE</span></div>
  <div class="side-label back"><span>BACK SIDE</span></div>

  <section class="size-card card-1">
    <div class="brand-ring"><div class="brand-name">KELMO<br>Coffee</div></div>
    <div class="size-lettering" role="img" aria-label="Hand-lettered word TINY"></div>
    <div class="size-band"><span>L</span><span>A</span><span>R</span><span>K</span></div>
  </section>
  <section class="size-card card-2">
    <div class="brand-ring"><div class="brand-name">KELMO<br>Coffee</div></div>
    <div class="size-lettering" role="img" aria-label="Hand-lettered word MID"></div>
    <div class="size-band"><span>W</span><span>R</span><span>E</span><span>N</span></div>
  </section>
  <section class="size-card card-3">
    <div class="brand-ring"><div class="brand-name">KELMO<br>Coffee</div></div>
    <div class="size-lettering" role="img" aria-label="Hand-lettered word TALL"></div>
    <div class="size-band"><span>H</span><span>E</span><span>R</span><span>O</span><span>N</span></div>
  </section>

  <section class="back-panel back-1">
    <div class="brand-ring"><div class="brand-name">KELMO<br>Coffee</div></div>
    <p class="story">Read about your<br>coffee and the<br>dedicated farmers<br>who made this cup<br>possible :</p>
    <p class="web">www.kelmo.com</p>
    <p class="social">@kelmocom</p>
  </section>
  <section class="back-panel back-2">
    <div class="brand-ring"><div class="brand-name">KELMO<br>Coffee</div></div>
    <p class="story">Read about your<br>coffee and the<br>dedicated farmers<br>who made this cup<br>possible :</p>
    <p class="web">www.kelmo.com</p>
    <p class="social">@kelmocom</p>
  </section>
  <section class="back-panel back-3">
    <div class="brand-ring"><div class="brand-name">KELMO<br>Coffee</div></div>
    <p class="story">Read about your<br>coffee and the<br>dedicated farmers<br>who made this cup<br>possible :</p>
    <p class="web">www.kelmo.com</p>
    <p class="social">@kelmocom</p>
  </section>

  <div class="die-cut-title">DIE CUT</div>

  <svg class="die-cut-art" width="1200" height="857" viewBox="0 0 1200 857">
    <!-- front sleeve -->
    <g class="sleeve-front">
      <path d="M890,258 Q1016,226 1140,258 L1099,409 Q1016,385 933,409 Z" fill="var(--kraft)" stroke="var(--bleed)" stroke-width="1.2"/>
      <path d="M895,262 Q1016,231 1135,262 L1096,404 Q1016,381 936,404 Z" fill="none" stroke="var(--margin)" stroke-width="0.6"/>
      <path d="M980,380 V290 A36,36 0 0 1 1052,290 V380 Z" fill="none" stroke="var(--brown)" stroke-width="1"/>
      <circle cx="1016" cy="289" r="33" fill="none" stroke="var(--brown)" stroke-width="1.6"/>
      <text x="1016" y="287" text-anchor="middle" font-size="10" font-weight="600" fill="var(--brown)">KELMO</text>
      <text x="1016" y="298" text-anchor="middle" font-size="10" font-weight="600" fill="var(--brown)">Coffee</text>
      <rect x="988" y="327" width="56" height="30" fill="#c9a98a" role="img" aria-label="Hand-lettered word TINY"/>
      <rect x="980" y="360" width="72" height="12" fill="var(--brown)"/>
      <text x="1016" y="369" text-anchor="middle" font-size="7" fill="var(--kraft)" letter-spacing="6">LARK</text>
    </g>
    <!-- back sleeve -->
    <g class="sleeve-back">
      <path d="M890,462 Q1016,430 1140,462 L1099,613 Q1016,589 933,613 Z" fill="var(--kraft)" stroke="var(--bleed)" stroke-width="1.2"/>
      <path d="M895,466 Q1016,435 1135,466 L1096,608 Q1016,585 936,608 Z" fill="none" stroke="var(--margin)" stroke-width="0.6"/>
      <circle cx="1016" cy="489" r="19" fill="none" stroke="var(--brown)" stroke-width="1.2"/>
      <text x="1016" y="488" text-anchor="middle" font-size="6" font-weight="600" fill="var(--brown)">KELMO</text>
      <text x="1016" y="495" text-anchor="middle" font-size="6" font-weight="600" fill="var(--brown)">Coffee</text>
      <g font-size="7" fill="var(--brown)" text-anchor="middle">
        <text x="1016" y="524">Read about your</text>
        <text x="1016" y="533">coffee and the</text>
        <text x="1016" y="541">dedicated farmers</text>
        <text x="1016" y="550">who made this cup</text>
        <text x="1016" y="559">possible :</text>
        <text x="1016" y="569" font-weight="600">www.kelmo.com</text>
        <text x="1016" y="581" font-weight="600">@kelmocom</text>
      </g>
    </g>
    <!-- bleed marker -->
    <g class="bleed-marker" stroke="var(--bleed)" fill="var(--bleed)">
      <line x1="1016" y1="401" x2="1016" y2="412" stroke-width="0.8"/>
      <path d="M1016,398 l-2,4 h4 Z" stroke="none"/>
      <line x1="1016" y1="430" x2="1016" y2="441" stroke-width="0.8"/>
      <path d="M1016,444 l-2,-4 h4 Z" stroke="none"/>
    </g>
    <text x="1015" y="427" text-anchor="middle" font-size="12" fill="var(--bleed)">Bleed</text>
    <!-- margin bracket -->
    <polyline points="1118,334 1145,334 1145,413" fill="none" stroke="var(--margin)" stroke-width="0.6"/>
    <polyline points="1145,432 1145,561 1110,561" fill="none" stroke="var(--margin)" stroke-width="0.6"/>
    <text x="1146" y="427" text-anchor="middle" font-size="12" fill="var(--margin)">Margin</text>
  </svg>
</body>
</html>
```